Design a product reviews website

We need a website design and simple logo for the brand Pivlo.com. The website will provide reviews of technology products and services. The brand and website should be approachable but should also be trustworthy and high quality. The deliverable should be designs, specs and assets that I can provide to a development team to build the website.

Target Market(s)

People researching products to buy.

Industry/Entity Type

Product

Logo Text

Pivlo.com

Number of Pages Required

5+ page

Font styles to use
Sans Serif

Colors
0492cd
0355a3
3176b5
33a6d7
85cae6
85abd2
cedeed
cee9f5

Requirements
Must have
• - Designs for the Homepage, Category and Article pages.
• - Designs for web and mobile.
• - Designs details for the engineering team to use for development.
• - I'm open to other colors than the preferences I chose but I'm more likely to like blues, greys and blacks.

```html
<!DOCTYPE html>
<html lang="en">
<head>
<meta charset="utf-8">
<title>Pivlo – Product Reviews</title>
<link href="https://fonts.googleapis.com/css2?family=Open+Sans:ital,wght@0,400;0,600;0,700;1,400&family=Roboto+Condensed:wght@700&display=swap" rel="stylesheet">
<style>
:root{
  --blue:#0492cd;
  --blue-dark:#0355a3;
  --blue-mid:#3176b5;
  --ink:#333;
  --text:#555;
  --muted:#888;
  --line:#dcdcdc;
  --panel:#f2f2f2;
  --white:#fff;
}
*{margin:0;padding:0;box-sizing:border-box}
html,body{width:723px;height:1200px;overflow:hidden}
body{position:relative;background:var(--white);font-family:"Open Sans",Arial,sans-serif;color:var(--text)}
.abs{position:absolute}

/* header */
.site-header{top:0;left:0;width:723px;height:51px;background:var(--white)}
.brand{left:58px;top:11px;font-size:27px;font-weight:700;color:var(--ink);letter-spacing:-.5px;display:flex;align-items:center;gap:6px}
.brand .dot{width:9px;height:9px;background:var(--blue);border-radius:2px}
.search-input{left:158px;top:16px;width:164px;height:20px;border:1px solid #ccc;border-radius:2px;font-size:7px;color:var(--muted);padding:5px 8px}
.search-btn{left:328px;top:16px;width:60px;height:20px;background:var(--blue);border-radius:2px;color:var(--white);font-size:7px;font-weight:700;display:flex;align-items:center;justify-content:center;gap:4px}
.menu-toggle{left:648px;top:20px}

/* hero */
.hero{top:51px;left:0;width:723px;height:264px;background:linear-gradient(180deg,#6c6a66 0%,#8d8a84 40%,#4a4744 75%,#3b3835 100%)}
.hero-window{left:193px;top:10px;width:312px;height:180px;background:linear-gradient(180deg,#c7ccce 0%,#b6b8b0 60%,#8e8f86 100%);opacity:.8}
.hero-brand{left:0;width:723px;top:95px;text-align:center;font-size:36px;font-weight:700;color:var(--white)}
.hero-title{left:0;width:723px;top:147px;text-align:center;font-family:"Roboto Condensed",Arial,sans-serif;font-weight:700;font-size:19px;line-height:21px;color:var(--white);text-transform:uppercase}

/* sidebar */
.cat-nav{left:58px;top:336px;width:102px;border:1px solid #e4e4e4}
.cat-nav li{list-style:none;height:23.3px;display:flex;align-items:center;gap:8px;padding-left:10px;font-size:8.5px;color:var(--text);border-top:1px solid #eee}
.cat-nav li:nth-child(even){background:#fafafa}
.cat-nav li.active{background:var(--blue);color:var(--white);font-weight:600;height:24px;border-top:none}
.cat-nav svg{width:9px;height:9px;flex:none}

/* sections */
.section-head{font-size:12px;font-weight:700;color:var(--ink);letter-spacing:.5px;padding-bottom:8px;border-bottom:1px solid var(--line)}
.new-head{left:184px;top:333px;width:320px}
.popular-head{left:526px;top:333px;width:138px}

.photo{background:#999}
.tag{position:absolute;background:var(--blue);color:var(--white);font-weight:700;text-transform:uppercase;display:flex;align-items:center;justify-content:center}
.tag-lg{height:15px;font-size:6.5px;padding:0 8px}
.tag-sm{height:11px;font-size:5px;padding:0 7px}

.feature-title{font-size:10px;color:var(--ink)}
.byline{display:flex;align-items:center;gap:8px;font-size:8px;font-style:italic;color:var(--text)}
.avatar{width:21px;height:21px;border-radius:50%;background:#c9c2ba;border:1px solid #ddd}
.byline .meta-icons{font-style:normal;color:#bbb;font-size:8px;margin-left:4px}

.thumb-caption{font-size:8px;line-height:11.5px;color:var(--ink)}
.pop-caption{font-size:9px;line-height:11.5px;color:var(--ink)}

/* footer */
.site-footer{top:1003px;left:0;width:723px;height:163px;background:var(--panel)}
.foot-brand{left:66px;top:1040px;font-size:32px;font-weight:700;color:var(--ink);display:flex;align-items:center;gap:6px}
.foot-brand .dot{width:10px;height:10px;background:var(--blue);border-radius:2px}
.social{left:68px;top:1095px;display:flex;gap:3px}
.social span{width:15px;height:15px;border:1px solid #555;border-radius:50%}
.foot-title{font-size:11.5px;color:var(--ink)}
.foot-title em{font-style:normal;color:var(--blue)}
.news-text{left:217px;top:1050px;width:158px;font-size:6.5px;line-height:11px;color:var(--text)}
.field{background:var(--white);border:1px solid #e6e6e6;font-size:6.5px;color:var(--text);padding:0 8px;display:flex;align-items:center}
.subscribe{left:317px;top:1120px;width:59px;height:24px;background:var(--blue);color:var(--white);font-size:8px;display:flex;align-items:center;justify-content:center}
.contact-list li{list-style:none;display:flex;gap:8px;font-size:8px;line-height:12px;color:var(--text);margin-bottom:8px}
.contact-list svg{width:8px;height:9px;flex:none;margin-top:2px}
.quick-links li{list-style:none;font-size:6.5px;line-height:13.5px;color:var(--text)}
.copyright{top:1166px;left:0;width:723px;height:34px;background:var(--blue);color:var(--white);font-size:6.5px;display:flex;align-items:center;justify-content:center}
</style>
</head>
<body>

<header class="abs site-header">
  <div class="abs brand"><span class="dot"></span>Pivlo</div>
  <div class="abs search-input">Enter your keyword</div>
  <div class="abs search-btn">
    <svg width="8" height="8" viewBox="0 0 10 10"><circle cx="4" cy="4" r="3" fill="none" stroke="#fff" stroke-width="1.4"/><line x1="6.3" y1="6.3" x2="9" y2="9" stroke="#fff" stroke-width="1.4"/></svg>SEARCH
  </div>
  <svg class="abs menu-toggle" width="15" height="12" viewBox="0 0 15 12"><g stroke="#888" stroke-width="1.2"><line x1="0" y1="1" x2="15" y2="1"/><line x1="0" y1="6" x2="15" y2="6"/><line x1="0" y1="11" x2="15" y2="11"/></g></svg>
</header>

<section class="abs hero" role="img" aria-label="Modern living room with dark sofas, tall windows and a wall-mounted TV">
  <div class="abs hero-window"></div>
</section>
<div class="abs hero-brand">Pivlo</div>
<h1 class="abs hero-title">The best product and services<br>reviews and rankings</h1>

<ul class="abs cat-nav">
  <li class="active"><svg viewBox="0 0 10 10"><path d="M5 1 1 5h1.5v4h2V6.5h1V9h2V5H9z" fill="#fff"/></svg>Home</li>
  <li><svg viewBox="0 0 10 10"><rect x="1" y="2" width="8" height="6" fill="none" stroke="#555"/><line x1="5" y1="2" x2="5" y2="8" stroke="#555"/></svg>Appliances</li>
  <li><svg viewBox="0 0 10 10"><rect x="1" y="1.5" width="8" height="5.5" fill="none" stroke="#555"/><line x1="3" y1="9" x2="7" y2="9" stroke="#555"/></svg>Computers</li>
  <li><svg viewBox="0 0 10 10"><circle cx="5" cy="4" r="2.7" fill="none" stroke="#555"/><line x1="5" y1="7" x2="5" y2="9.5" stroke="#555"/></svg>Electronics</li>
  <li><svg viewBox="0 0 10 10"><rect x="2" y="4.5" width="6" height="5" fill="#555"/><path d="M3.3 4.5V3a1.7 1.7 0 0 1 3.4 0v1.5" fill="none" stroke="#555"/></svg>Home security</li>
  <li><svg viewBox="0 0 10 10"><rect x="3" y="1" width="4" height="8" rx=".6" fill="none" stroke="#555"/></svg>Mobile</li>
  <li><svg viewBox="0 0 10 10"><circle cx="5" cy="5" r="3" fill="none" stroke="#555" stroke-width="2" stroke-dasharray="1.5 1"/><circle cx="5" cy="5" r="1" fill="#555"/></svg>Smart Home</li>
  <li><svg viewBox="0 0 10 10"><rect x=".5" y="2.5" width="9" height="5" fill="none" stroke="#555"/><line x1="2" y1="5" x2="8" y2="5" stroke="#555" stroke-dasharray="1 .6"/></svg>Software</li>
</ul>

<h2 class="abs section-head new-head">NEW</h2>
<h2 class="abs section-head popular-head">POPULAR</h2>

<!-- new: feature 1 -->
<div class="abs photo" style="left:183px;top:367px;width:321px;height:177px;background:linear-gradient(90deg,#c8453a 0%,#d4564a 45%,#e4e6ea 70%,#b8a89a 100%)" role="img" aria-label="Living room with a red accent wall, TV console and grey sofa"></div>
<span class="tag tag-lg" style="left:402px;top:519px">Home</span>
<span class="tag tag-lg" style="left:447px;top:519px">Speakers</span>
<p class="abs feature-title" style="left:183px;top:551px">Nemo enim ipsam voluptatem quia voluptas sit</p>
<div class="abs byline" style="left:183px;top:571px"><span class="avatar" role="img" aria-label="Author portrait"></span>By Mara Linde,&nbsp;&nbsp; July 18, 2016<span class="meta-icons">⇣ &nbsp;|&nbsp; ↱</span></div>

<!-- new: thumbs -->
<div class="abs photo" style="left:183px;top:609px;width:100px;height:85px;background:linear-gradient(90deg,#5a4a3c,#8a7a6a 60%,#c8cdd0)" role="img" aria-label="Dark modern kitchen with pendant lights"></div>
<span class="tag tag-sm" style="left:240px;top:678px">Home</span>
<p class="abs thumb-caption" style="left:183px;top:702px;width:100px">Nemo enim ipsam volupt quia voluptas sit</p>

<div class="abs photo" style="left:293px;top:609px;width:100px;height:85px;background:linear-gradient(180deg,#6d6d6d,#8f8f8f 60%,#cfcfcf)" role="img" aria-label="Grey lounge with wall art and white sofa"></div>
<span class="tag tag-sm" style="left:350px;top:678px">Audio</span>
<p class="abs thumb-caption" style="left:293px;top:702px;width:100px">Nemo enim ipsam volupt quia voluptas sit</p>

<div class="abs photo" style="left:403px;top:609px;width:100px;height:85px;background:linear-gradient(180deg,#8a6548,#a57c5a 55%,#d8c7a0)" role="img" aria-label="Warm wood-panelled room with yellow sofa"></div>
<span class="tag tag-sm" style="left:460px;top:678px">Home</span>
<p class="abs thumb-caption" style="left:403px;top:702px;width:100px">Nemo enim ipsam volupt quia voluptas sit</p>

<!-- new: feature 2 -->
<div class="abs photo" style="left:183px;top:747px;width:321px;height:177px;background:linear-gradient(90deg,#b8a48a 0%,#dcc9ac 40%,#e8d8bc 65%,#a08466 100%)" role="img" aria-label="Beige living room with fireplace, stacked logs and white sofa"></div>
<span class="tag tag-lg" style="left:402px;top:900px">Home</span>
<span class="tag tag-lg" style="left:447px;top:900px">Speakers</span>
<p class="abs feature-title" style="left:183px;top:931px">Nemo enim ipsam voluptatem quia voluptas sit</p>
<div class="abs byline" style="left:183px;top:951px"><span class="avatar" role="img" aria-label="Author portrait"></span>By Mara Linde,&nbsp;&nbsp; July 18, 2016<span class="meta-icons">⇣ &nbsp;|&nbsp; ↱</span></div>

<!-- popular -->
<div class="abs photo" style="left:526px;top:367px;width:138px;height:106px;background:linear-gradient(90deg,#d8d8d6,#b9bdb8 55%,#6c655c)" role="img" aria-label="Bright lounge with white sofa and stone fireplace"></div>
<span class="tag tag-lg" style="left:615px;top:450px">Home</span>
<p class="abs pop-caption" style="left:526px;top:479px;width:138px">Nemo enim ipsam voluptatem quia voluptas sit</p>

<div class="abs photo" style="left:526px;top:521px;width:138px;height:106px;background:linear-gradient(180deg,#c9b67a,#a78d62 55%,#6e5a44)" role="img" aria-label="Home theatre room with projector and large sofa"></div>
<span class="tag tag-lg" style="left:615px;top:604px">Audio</span>
<p class="abs pop-caption" style="left:526px;top:634px;width:138px">Nemo enim ipsam voluptatem quia voluptas sit</p>

<div class="abs photo" style="left:526px;top:677px;width:138px;height:106px;background:linear-gradient(90deg,#6a6a6a,#a9adad 50%,#dfe3e4)" role="img" aria-label="Seaside living room with grey sofa and curtains"></div>
<span class="tag tag-lg" style="left:615px;top:758px">Home</span>
<p class="abs pop-caption" style="left:526px;top:789px;width:138px">Nemo enim ipsam voluptatem quia voluptas sit</p>

<div class="abs photo" style="left:526px;top:837px;width:138px;height:106px;background:linear-gradient(180deg,#8e7c6a,#b7a795 55%,#e2ddd6)" role="img" aria-label="Stone wall living room with white sofa"></div>
<span class="tag tag-lg" style="left:615px;top:918px">Audio</span>
<p class="abs pop-caption" style="left:526px;top:949px;width:138px">Nemo enim ipsam voluptatem quia voluptas sit</p>

<!-- footer -->
<footer class="abs site-footer"></footer>
<div class="abs foot-brand"><span class="dot"></span>Pivlo</div>
<div class="abs social"><span></span><span></span><span></span><span></span><span></span></div>

<h3 class="abs foot-title" style="left:217px;top:1028px">Sign Up For <em>Newsletter</em></h3>
<p class="abs news-text">Excepteur sint occaecat cupidatat non proident, sunt in culpa qui officia deserunt</p>
<div class="abs field" style="left:217px;top:1081px;width:158px;height:25px">Enter Name</div>
<div class="abs field" style="left:217px;top:1120px;width:100px;height:24px">Enter Email</div>
<div class="abs subscribe">SUBSCRIBE</div>

<h3 class="abs foot-title" style="left:427px;top:1028px">Contacts <em>Us</em></h3>
<ul class="abs contact-list" style="left:427px;top:1053px;width:150px">
  <li><svg viewBox="0 0 8 10"><path d="M4 .5a3 3 0 0 0-3 3c0 2.3 3 6 3 6s3-3.7 3-6a3 3 0 0 0-3-3z" fill="#aaa"/><circle cx="4" cy="3.5" r="1" fill="#f2f2f2"/></svg><span style="font-size:7.5px">Pivlo , Elm Court<br>Harbor Lane ,</span></li>
  <li><svg viewBox="0 0 8 10"><path d="M1.5 1 3 .8l1 2.3-1 .9c.5 1.3 1.2 2.1 2.3 2.7l.9-1 2 1.2-.3 1.6C4.5 8.4 .4 4.4 1.5 1z" fill="#aaa"/></svg>Phone: (555) 014-2290</li>
  <li><svg viewBox="0 0 8 10"><rect x=".5" y="2.5" width="7" height="5" fill="#aaa"/><path d="M.5 2.5 4 5.5l3.5-3" fill="none" stroke="#f2f2f2" stroke-width=".7"/></svg>hello@pivlo.com</li>
</ul>

<h3 class="abs foot-title" style="left:599px;top:1028px">Quick <em>Links</em></h3>
<ul class="abs quick-links" style="left:601px;top:1049px">
  <li>Appliances</li><li>Computers</li><li>Electronics</li><li>Home security</li><li>Mobile</li><li>Smart Home</li>
</ul>

<div class="abs copyright">©2015 - 2016 Pivlo. All Rights Reserved.</div>

</body>
</html>
```